Australian HR Consultancy Company Brochure (and more!). Our tagline "Start something amazing."

We are a start-up HR and Recruitment consultancy. We have a group of young, passionate and top performing staff who assist companies with driving their workforce productivity, keeping employees happy, hiring fantastic people and ensuring legal compliance across the HR field.

We work across a variety of sectors such as mining, Not for Profits, Finance, Accounting, Health etc so are not pigeon-holed to one particular group. We tend to deal with medium sized businesses.

Our team is professional and corporate but down to earth and approachable. We have unique offerings in terms of our services and our pricing. We deliver exceptional value to our clients and build long term mutually beneficial relationships. We care about giving back to the community and doing the right thing by everyone we deal with.

Our design should communicate that we are corporate and professional but not uptight 'suits', that we are fresh and engaging. Clear, concise, crisp but not cold.

Thinking 6 page brochure.

We have a variety of colours in our logo and tend to lean towards fresh shades of blue and green but are definitely open to other colours such as purple, pink, orange etc. We would prefer the brochure to be in landscape format (like a powerpoint presentation) as apparently that's easier to read? but open to your expert suggestions!

Target Market(s)

Medium sized business across all industries but within the professional area ie finance, mining, health.

Industry/Entity Type

It Company

Colors
33b8a4
33a6d7
0592cd
85cae6
86cfc6
b768aa

Requirements
Must have
• Needs to be editable version as we will be changing our tagline and about us in the new year.

```html
<!DOCTYPE html>
<html lang="en">
<head>
<meta charset="utf-8">
<title>TeamLaunch brochure pages</title>
<link href="https://fonts.googleapis.com/css2?family=Montserrat:wght@300;400;500;600;700;800&family=Open+Sans:wght@400;600&display=swap" rel="stylesheet">
<style>
  :root{
    --navy:#2b3852;
    --navy-deep:#1f2b45;
    --green:#7cc43a;
    --orange:#f7941d;
    --slate:#5d6188;
    --royal:#2f3a8f;
    --ink:#3a3f4a;
    --stage-top:#8d8d8d;
    --stage-bottom:#a6a6a6;
    --white:#ffffff;
  }
  *{margin:0;padding:0;box-sizing:border-box}
  html,body{width:1200px;height:969px;overflow:hidden}
  body{
    background:linear-gradient(180deg,var(--stage-top),var(--stage-bottom));
    font-family:"Montserrat",sans-serif;
    position:relative;
  }
  .page{
    position:absolute;width:538px;height:380px;overflow:hidden;background:var(--white);
    box-shadow:0 14px 18px -8px rgba(0,0,0,.45);
  }
  .page--back{left:42px;top:42px}
  .page--cover{left:620px;top:42px}
  .page--about{left:42px;top:506px}
  .page--services{left:620px;top:506px}
  .page-label{
    position:absolute;width:538px;text-align:center;color:var(--white);
    font-weight:400;font-size:19px;letter-spacing:.3px;
  }
  .abs{position:absolute}
  .art{position:absolute;left:0;top:0}
  .brand{font-family:"Montserrat",sans-serif;font-weight:600;letter-spacing:-.5px;white-space:nowrap}
  .brand-dot{position:absolute;border-radius:50%;background:var(--orange)}

  /* back page */
  .back-photo{position:absolute;inset:0;background:linear-gradient(120deg,#2f3e5c 0%,#26344f 55%,#33425f 100%)}
  .back-invite{left:198px;top:140px;color:var(--white);font-size:13px}
  .back-brand{left:170px;top:152px;color:var(--white);font-size:44px}
  .back-team{left:0;width:538px;top:250px;text-align:center;color:var(--white)}
  .back-team p{font-size:14px;font-weight:400;margin-left:-16px}
  .back-team strong{display:block;color:var(--orange);font-size:19px;font-weight:700;margin-top:3px;margin-left:-16px}
  .back-contact{left:113px;top:336px;color:var(--white);font-size:13px;display:flex;align-items:center;gap:6px}
  .back-contact .sep{margin:0 4px}

  /* cover */
  .cover-brand{left:96px;top:40px;color:var(--navy);font-size:32px}
  .cover-head{left:16px;top:128px;color:var(--white);line-height:1}
  .cover-head .light{font-weight:300;font-size:31px;display:block;margin-bottom:3px}
  .cover-head .bold{font-weight:800;font-size:39px;color:var(--green);display:block;margin-top:2px}
  .cover-welcome{left:16px;top:257px;color:var(--white);font-size:11px}
  .cover-welcome strong{display:block;color:var(--green);font-size:14px;font-weight:700;margin-top:1px}
  .cover-url{left:21px;top:349px;font-family:"Open Sans",sans-serif;font-size:10px;letter-spacing:.8px;color:var(--ink)}

  /* about */
  .about-brand{left:58px;top:25px;color:var(--navy-deep);font-size:16px}
  .about-title{left:34px;top:77px;font-size:29px;font-weight:800;color:var(--orange)}
  .about-title span{font-weight:400;color:var(--slate)}
  .about-body{left:23px;top:120px;width:213px;font-family:"Open Sans",sans-serif;font-size:9.6px;line-height:13px;color:var(--ink);text-align:justify}
  .about-body p+p{margin-top:7px}
  .about-body b{color:var(--slate);font-weight:600}
  .page-no{position:absolute;width:15px;height:15px;border:1px solid var(--orange);font-size:9px;display:flex;align-items:center;justify-content:center;color:var(--ink);background:var(--white)}

  /* services */
  .svc-brand{left:48px;top:25px;color:var(--navy-deep);font-size:16px}
  .svc-vertical{left:16px;top:342px;transform:rotate(-90deg);transform-origin:left top;font-size:32px;font-weight:800;color:var(--slate);letter-spacing:.5px;white-space:nowrap}
  .svc-kicker{left:58px;top:60px;font-size:10px;font-weight:700;color:var(--orange)}
  .svc-intro{left:58px;top:74px;width:240px;font-family:"Open Sans",sans-serif;font-size:8.8px;line-height:12px;color:var(--ink)}
  .svc-item{position:absolute;width:140px;text-align:center;font-size:9.8px;line-height:13px;font-weight:500;color:#2a2d36}
  .svc-item span{display:block;color:var(--royal)}
  .svc-plus{position:absolute;color:#b8b8c0;font-size:15px;font-weight:300}
</style>
</head>
<body>

<!-- BACK PAGE -->
<section class="page page--back">
  <div class="back-photo" role="img" aria-label="Dimmed photo of a presenter speaking to a seated audience, navy tint"></div>
  <div class="brand-dot" style="left:82px;top:170px;width:66px;height:66px"></div>
  <p class="abs back-invite">Start a conversation with us</p>
  <p class="abs brand back-brand">TeamLaunch</p>
  <div class="abs back-team">
    <p>Our Leadership Team</p>
    <strong>ALEX, MAYA, JONO</strong>
  </div>
  <p class="abs back-contact">
    <svg width="11" height="11" viewBox="0 0 11 11"><circle cx="5.5" cy="5.5" r="5.5" fill="#f7941d"/><path d="M3.5 3 l1.2 0 .5 1.3-.7.5a4 4 0 0 0 1.7 1.7l.5-.7 1.3.5v1.2A4.6 4.6 0 0 1 3.5 3z" fill="#2b3852"/></svg>
    1300 555 019 <span class="sep">|</span>
    <svg width="11" height="11" viewBox="0 0 11 11"><circle cx="5.5" cy="5.5" r="5.5" fill="#f7941d"/><circle cx="5.5" cy="5.5" r="2" fill="#2b3852"/></svg>
    WWW.TEAMLAUNCH.COM.AU
  </p>
</section>
<p class="page-label" style="left:42px;top:446px">BACK PAGE</p>

<!-- COVER PAGE -->
<section class="page page--cover">
  <svg class="art" width="539" height="380" viewBox="0 0 539 380">
    <defs>
      <linearGradient id="officeTone" x1="0" y1="0" x2="1" y2="1">
        <stop offset="0" stop-color="#f1f1ef"/>
        <stop offset=".5" stop-color="#d9d8d4"/>
        <stop offset="1" stop-color="#b9b6b0"/>
      </linearGradient>
    </defs>
    <polygon points="300,0 539,0 539,380 262,380 240,300" fill="url(#officeTone)" role="img" aria-label="Photo of a bright modern office with desks, monitors and chairs"/>
    <polygon points="0,105 193,105 190,110 0,110" fill="#7cc43a"/>
    <polygon points="0,110 264,110 222,295 0,295" fill="#2b3852"/>
    <polygon points="88,295 268,295 266,301 90,301" fill="#7cc43a"/>
    <line x1="16" y1="241" x2="76" y2="241" stroke="#7cc43a" stroke-width="1.5"/>
    <line x1="168" y1="356" x2="270" y2="356" stroke="#f7941d" stroke-width="1"/>
  </svg>
  <div class="brand-dot" style="left:28px;top:28px;width:56px;height:56px"></div>
  <p class="abs brand cover-brand">TeamLaunch</p>
  <h1 class="abs cover-head">
    <span class="light">START</span>
    <span class="light">SOMETHING</span>
    <span class="bold">AMAZING</span>
  </h1>
  <p class="abs cover-welcome">WELCOME TO<strong>TEAMLAUNCH, YOUR HR TEAM</strong></p>
  <p class="abs cover-url">www.teamlaunch.com.au</p>
</section>
<p class="page-label" style="left:620px;top:446px">COVER PAGE</p>

<!-- PAGE 1 -->
<section class="page page--about">
  <svg class="art" width="538" height="380" viewBox="0 0 538 380">
    <defs>
      <linearGradient id="roomTone" x1="0" y1="0" x2="1" y2="1">
        <stop offset="0" stop-color="#f4f4f4"/>
        <stop offset=".55" stop-color="#dcdcdc"/>
        <stop offset="1" stop-color="#9c9a98"/>
      </linearGradient>
    </defs>
    <polygon points="306,0 538,0 538,380 226,380" fill="url(#roomTone)" role="img" aria-label="Photo of a woman presenting at a whiteboard to a seated group"/>
    <polygon points="304,0 310,0 296,86 290,86" fill="#5d6188"/>
    <polygon points="254,246 264,246 218,380 208,380" fill="#f7941d"/>
    <rect x="0" y="82" width="27" height="20" fill="#5d6188"/>
    <line x1="24" y1="355" x2="538" y2="355" stroke="#f7941d" stroke-width="1"/>
  </svg>
  <div class="brand-dot" style="left:30px;top:24px;width:22px;height:22px"></div>
  <p class="abs brand about-brand">TeamLaunch</p>
  <h2 class="abs about-title">ABOUT <span>US</span></h2>
  <div class="abs about-body">
    <p><b>TEAMLAUNCH</b> is an innovative industry leader in the provision of human resources, industrial relations and recruitment managed services. Our unique approach enables us to meet the challenges and demands of a diverse group of a contemporary Australian businesses.</p>
    <p>We are committed to delivering exceptional service and value that ensures the best outcomes for our long-term business partnerships.</p>
  </div>
  <div class="page-no" style="left:24px;top:348px">1</div>
</section>
<p class="page-label" style="left:42px;top:916px">PAGE 1</p>

<!-- PAGE 2 -->
<section class="page page--services">
  <svg class="art" width="539" height="380" viewBox="0 0 539 380">
    <defs>
      <linearGradient id="meetTone" x1="0" y1="0" x2="1" y2="1">
        <stop offset="0" stop-color="#4a5a86"/>
        <stop offset=".6" stop-color="#2f3f68"/>
        <stop offset="1" stop-color="#1e2a4a"/>
      </linearGradient>
    </defs>
    <polygon points="276,0 539,0 539,380 292,380 360,202" fill="url(#meetTone)" role="img" aria-label="Photo of two businessmen reviewing documents together"/>
    <polygon points="276,0 286,0 318,74 308,74" fill="#5d6188" opacity=".9"/>
    <polygon points="336,262 340,262 292,380 282,380" fill="#f7941d"/>
    <line x1="0" y1="355" x2="498" y2="355" stroke="#f7941d" stroke-width="1"/>
    <g fill="#f7941d">
      <!-- handshake -->
      <path d="M101 124 l8-6 6 3 6-3 8 6-8 7-6-3-6 3z"/>
      <!-- person up -->
      <circle cx="243" cy="113" r="3"/><rect x="234" y="120" width="18" height="6" rx="2"/><rect x="241" y="116" width="4" height="6"/>
      <!-- tools -->
      <path d="M104 178 l16 16-3 3-16-16z M120 178 l3 3-16 16-3-3z"/>
      <!-- thumbs up -->
      <path d="M236 182 h5 l3-7 h3 v6 h6 l-2 11 h-15z"/>
      <!-- person alert -->
      <circle cx="110" cy="243" r="4.5"/><path d="M102 258 a8 7 0 0 1 16 0z"/><circle cx="121" cy="239" r="4"/>
      <!-- documents -->
      <rect x="236" y="239" width="11" height="14" rx="1"/><rect x="241" y="236" width="11" height="14" rx="1" fill="none" stroke="#f7941d" stroke-width="1.5"/>
      <!-- team -->
      <circle cx="104" cy="301" r="3"/><circle cx="112" cy="299" r="3.5"/><circle cx="120" cy="301" r="3"/><path d="M99 312 a5 5 0 0 1 26 0z"/>
      <!-- magnifier -->
      <circle cx="242" cy="302" r="6" fill="none" stroke="#f7941d" stroke-width="2"/><path d="M246 306 l6 6-2 2-6-6z"/>
    </g>
  </svg>
  <div class="brand-dot" style="left:20px;top:24px;width:22px;height:22px"></div>
  <p class="abs brand svc-brand">TeamLaunch</p>
  <p class="abs svc-vertical">HR CONSULTING</p>
  <p class="abs svc-kicker">HR FOUNDATIONS</p>
  <p class="abs svc-intro">Building the HR foundations for legal compliance &amp; employee management</p>

  <p class="svc-item" style="left:42px;top:141px">Employment Contracts<span>&amp; Agreements</span></p>
  <p class="svc-item" style="left:172px;top:141px">Recruitment &amp;<span>Onboarding</span></p>
  <p class="svc-item" style="left:42px;top:203px">Organisational<span>Structure&amp; Design</span></p>
  <p class="svc-item" style="left:172px;top:203px">Remuneration<span>&amp; Benefits</span></p>
  <p class="svc-item" style="left:42px;top:265px">Terminations &amp;<span>Fair Work Advice</span></p>
  <p class="svc-item" style="left:172px;top:265px">HR Policies &amp;<span>Procedures</span></p>
  <p class="svc-item" style="left:42px;top:321px">Performance<span>Management</span></p>
  <p class="svc-item" style="left:172px;top:321px">Workplace<span>Investigations</span></p>

  <span class="svc-plus" style="left:177px;top:173px">+</span>
  <span class="svc-plus" style="left:177px;top:235px">+</span>
  <span class="svc-plus" style="left:177px;top:300px">+</span>

  <div class="page-no" style="left:498px;top:348px">2</div>
</section>
<p class="page-label" style="left:620px;top:916px">PAGE 2</p>

</body>
</html>
```